ROVA Pty Ltd Business Card

Looking for a simple yet eye-catching double-sided business card design using my company logo on one side and contact details on the other.

Target Market(s)

Government

Industry/Entity Type

Communication Systems Engineering

Contact Information for Business Card

ROVA Pty Ltd

Requirements
Nice to have
• Would be great to have a QR code so details can be scanned into contacts

```html
<!DOCTYPE html>
<html lang="en">
<head>
<meta charset="utf-8">
<title>ROVA Pty Ltd Business Card</title>
<link href="https://fonts.googleapis.com/css2?family=Poppins:wght@400;500;600&display=swap" rel="stylesheet">
<style>
  :root {
    --backdrop: #777777;
    --card-light: #ffffff;
    --card-dark: #374049;
    --ink: #313b43;
    --rule: #6d747a;
    --mark-tint: #46515a;
  }
  * { margin: 0; padding: 0; box-sizing: border-box; }
  html, body { width: 1065px; height: 1200px; overflow: hidden; }
  body {
    background: var(--backdrop);
    font-family: "Poppins", sans-serif;
    color: var(--ink);
    position: relative;
  }
  .card {
    position: absolute;
    width: 583px;
    height: 363px;
    box-shadow: 2px 3px 3px rgba(0,0,0,0.55);
  }
  .card--front {
    left: 292px; top: 218px;
    background: var(--card-light);
    border-radius: 0 181px 181px 0;
  }
  .card--back {
    left: 263px; top: 623px;
    background: var(--card-dark);
    border-radius: 181px 0 0 181px;
  }
  .brand-vertical {
    position: absolute;
    left: 408px; top: 431px;
    transform-origin: 0 0;
    transform: rotate(-90deg);
    font-weight: 600;
    font-size: 40px;
    line-height: 1;
    letter-spacing: 6px;
    color: var(--ink);
  }
  .brand-dot {
    position: absolute;
    left: 390px; top: 452px;
    width: 36px; height: 36px;
    border-radius: 50%;
    background: var(--ink);
  }
  .divider {
    position: absolute;
    left: 490px; top: 313px;
    width: 1px; height: 173px;
    background: var(--rule);
  }
  .details {
    position: absolute;
    left: 518px; top: 311px;
  }
  .details__name {
    font-weight: 600;
    font-size: 21px;
    line-height: 1.1;
    letter-spacing: 0.2px;
  }
  .details__role {
    font-size: 17px;
    line-height: 1.1;
    margin-bottom: 14px;
  }
  .details__contact {
    list-style: none;
    font-size: 17px;
    line-height: 21.5px;
  }
  .details__contact li { display: flex; align-items: center; }
  .details__contact svg { width: 15px; height: 15px; margin-right: 6px; fill: var(--ink); }
  .details__address {
    margin-top: 14px;
    font-size: 17px;
    line-height: 21.5px;
  }
  .brand-back-dot {
    position: absolute;
    left: 341px; top: 744px;
    width: 120px; height: 120px;
    border-radius: 50%;
    background: var(--mark-tint);
  }
  .brand-back {
    position: absolute;
    left: 496px; top: 772px;
    font-weight: 600;
    font-size: 82px;
    line-height: 1;
    letter-spacing: 8px;
    color: var(--card-light);
  }
</style>
</head>
<body>
  <section class="card card--front" aria-label="Business card front"></section>
  <div class="brand-vertical">ROVA</div>
  <div class="brand-dot"></div>
  <div class="divider"></div>
  <div class="details">
    <h1 class="details__name">DANIEL MERCER</h1>
    <p class="details__role">Managing Director</p>
    <ul class="details__contact">
      <li><svg viewBox="0 0 24 24"><path d="M6.6 10.8a15.1 15.1 0 0 0 6.6 6.6l2.2-2.2c.3-.3.7-.4 1-.2 1.1.4 2.3.6 3.6.6.6 0 1 .4 1 1V20c0 .6-.4 1-1 1A17 17 0 0 1 3 4c0-.6.4-1 1-1h3.5c.6 0 1 .4 1 1 0 1.3.2 2.5.6 3.6.1.3 0 .7-.2 1z"/></svg>044-987 654 321</li>
      <li><svg viewBox="0 0 24 24"><path d="M2 5h20v14H2z M2 6l10 7 10-7" stroke="#fff" stroke-width="1.5"/></svg>info@rovacomms.com</li>
      <li><svg viewBox="0 0 24 24"><circle cx="12" cy="12" r="10"/><path d="M2 12h20M12 2v20M5 6h14M5 18h14M12 2c-4 5-4 15 0 20M12 2c4 5 4 15 0 20" stroke="#fff" stroke-width="1.2" fill="none"/></svg>www.rovacomms.com</li>
    </ul>
    <p class="details__address">18, Harbour Point Drive<br>2000, Australia</p>
  </div>

  <section class="card card--back" aria-label="Business card back"></section>
  <div class="brand-back-dot"></div>
  <div class="brand-back">ROVA</div>
</body>
</html>
```